Business Card, Letterhead, Envelopes, Thank you cards, Post Cards
Business cards and stationary for life coach
Professional
Silver Heron Guidance Studio
Marla Penrick, MA
4810 North Calloway Avenue
Suite C 240
Missoula, Montana 59417
silverheronguidance@mailbox-example.net
silverheronguidance-example.com
I would like to see 'Let Your Dreams Take Flight' on the front of the card. This is the tagline. Please use a compatible font with the logo.
'Dragonfly spends most of her life underwater until the day she discovers her wings and soars upon the wind.' I'd like to see this in script, similar to the logo font.
Please let me know if you need different files.

```html
<!DOCTYPE html>
<html lang="en">
<head>
<meta charset="utf-8">
<title>Silver Heron Guidance Studio – Stationery</title>
<link rel="stylesheet" href="https://fonts.googleapis.com/css2?family=Open+Sans:wght@400;600&display=swap">
<style>
  :root {
    --bg: #eef1f4;
    --paper: #ffffff;
    --blue-deep: #1f5fc4;
    --blue-mid: #2f8fe0;
    --blue-light: #7cc6f2;
    --ink: #4a5563;
    --shadow: 0 4px 14px rgba(20, 40, 70, 0.22);
  }
  * { box-sizing: border-box; margin: 0; padding: 0; }
  html, body { width: 1200px; height: 679px; overflow: hidden; }
  body {
    background: var(--bg);
    font-family: "Open Sans", sans-serif;
    color: var(--ink);
    position: relative;
  }
  .piece {
    position: absolute;
    background: var(--paper);
    box-shadow: var(--shadow);
    overflow: hidden;
  }
  .piece svg.swoosh { position: absolute; inset: 0; width: 100%; height: 100%; }
  .brand {
    position: absolute;
    display: flex;
    align-items: center;
    gap: 6px;
    color: var(--blue-deep);
    font-weight: 600;
    line-height: 1.1;
  }
  .brand .dot {
    flex: none;
    border-radius: 50%;
    background: var(--blue-mid);
  }
  .small {
    position: absolute;
    font-size: 6px;
    line-height: 1.45;
    color: var(--ink);
  }

  /* business cards */
  .card { width: 264px; height: 144px; border-radius: 8px; }
  .card-front { left: 92px; top: 96px; }
  .card-front .brand { left: 16px; top: 22px; font-size: 12px; width: 130px; }
  .card-front .brand .dot { width: 14px; height: 14px; }
  .card-front .person { position: absolute; right: 18px; top: 26px; font-size: 8px; color: var(--ink); }
  .card-front .small { left: 16px; top: 70px; }

  .card-plain { left: 92px; top: 264px; }
  .card-plain .brand { left: 16px; top: 82px; font-size: 11px; width: 130px; }
  .card-plain .brand .dot { width: 12px; height: 12px; }

  .card-back {
    left: 92px; top: 432px;
    background: linear-gradient(135deg, var(--blue-mid), var(--blue-deep));
  }
  .card-back .brand { left: 16px; top: 88px; font-size: 11px; width: 140px; color: #fff; }
  .card-back .brand .dot { width: 12px; height: 12px; background: #fff; }

  /* letterhead */
  .letterhead { left: 384px; top: 91px; width: 259px; height: 509px; }
  .letterhead-under { left: 394px; top: 101px; width: 259px; height: 509px; box-shadow: var(--shadow); }
  .letterhead .brand { right: 16px; top: 20px; font-size: 10px; width: 112px; }
  .letterhead .brand .dot { width: 11px; height: 11px; }
  .letterhead .small { left: 16px; top: 452px; font-size: 5px; }

  /* envelopes */
  .envelope { width: 350px; height: 134px; }
  .envelope-flap {
    left: 748px; top: 206px;
    background: linear-gradient(160deg, #ffffff 35%, var(--blue-light) 60%, var(--blue-deep));
  }
  .envelope-flap .brand { left: 50%; transform: translateX(-50%); top: 16px; color: #fff; font-size: 9px; }
  .envelope-flap .brand .dot { width: 10px; height: 10px; background: #fff; }
  .envelope-back { left: 724px; top: 246px; }
  .envelope-front { left: 770px; top: 316px; }
  .envelope-front .brand { left: 14px; top: 14px; font-size: 9px; width: 120px; }
  .envelope-front .brand .dot { width: 10px; height: 10px; }
  .envelope-front .small { left: 14px; top: 44px; font-size: 5px; }
</style>
</head>
<body>

  <!-- business card: front -->
  <section class="piece card card-front">
    <svg class="swoosh" viewBox="0 0 264 144" preserveAspectRatio="none" aria-hidden="true">
      <defs>
        <linearGradient id="gFront" x1="0" y1="0" x2="1" y2="1">
          <stop offset="0" stop-color="#7cc6f2"/><stop offset="1" stop-color="#1f5fc4"/>
        </linearGradient>
      </defs>
      <path d="M130 144 C190 140 240 110 264 60 L264 144 Z" fill="url(#gFront)"/>
      <path d="M100 144 C170 138 230 112 264 70" fill="none" stroke="#2f8fe0" stroke-width="2"/>
    </svg>
    <div class="brand"><span class="dot"></span>Silver Heron Guidance Studio</div>
    <div class="person">Marla Penrick, MA</div>
    <p class="small">4810 North Calloway Avenue<br>Suite C 240<br>Missoula, Montana 59417<br>(406) 555-0142<br>silverheronguidance@mailbox-example.net</p>
  </section>

  <!-- business card: plain back -->
  <section class="piece card card-plain">
    <svg class="swoosh" viewBox="0 0 264 144" preserveAspectRatio="none" aria-hidden="true">
      <path d="M264 20 C230 60 200 110 180 144 L264 144 Z" fill="#2f8fe0" opacity="0.85"/>
      <path d="M264 5 C220 50 190 110 165 144" fill="none" stroke="#7cc6f2" stroke-width="2"/>
    </svg>
    <div class="brand"><span class="dot"></span>Silver Heron Guidance Studio</div>
  </section>

  <!-- business card: blue back -->
  <section class="piece card card-back">
    <svg class="swoosh" viewBox="0 0 264 144" preserveAspectRatio="none" aria-hidden="true">
      <path d="M0 40 C90 20 180 30 264 0 L264 0 L0 0 Z" fill="#ffffff" opacity="0.12"/>
    </svg>
    <div class="brand"><span class="dot"></span>Silver Heron Guidance Studio</div>
  </section>

  <!-- letterhead -->
  <div class="piece letterhead-under"></div>
  <section class="piece letterhead">
    <svg class="swoosh" viewBox="0 0 259 509" preserveAspectRatio="none" aria-hidden="true">
      <defs>
        <linearGradient id="gLetter" x1="0" y1="0" x2="1" y2="1">
          <stop offset="0" stop-color="#7cc6f2"/><stop offset="1" stop-color="#1f5fc4"/>
        </linearGradient>
      </defs>
      <path d="M110 509 C190 500 240 470 259 420 L259 509 Z" fill="url(#gLetter)"/>
      <path d="M80 509 C170 498 235 462 259 430" fill="none" stroke="#2f8fe0" stroke-width="2"/>
    </svg>
    <div class="brand"><span class="dot"></span>Silver Heron Guidance Studio</div>
    <p class="small">4810 North Calloway Avenue<br>Suite C 240, Missoula, Montana 59417<br>(406) 555-0142<br>silverheronguidance@mailbox-example.net</p>
  </section>

  <!-- envelope: flap side -->
  <section class="piece envelope envelope-flap">
    <svg class="swoosh" viewBox="0 0 350 134" preserveAspectRatio="none" aria-hidden="true">
      <path d="M0 0 L175 70 L350 0" fill="none" stroke="#ffffff" stroke-width="1.5"/>
    </svg>
    <div class="brand"><span class="dot"></span>Silver Heron</div>
  </section>

  <!-- envelope: plain back -->
  <section class="piece envelope envelope-back">
    <svg class="swoosh" viewBox="0 0 350 134" preserveAspectRatio="none" aria-hidden="true">
      <path d="M0 0 L175 62 L350 0" fill="none" stroke="#c9d2dc" stroke-width="1"/>
      <path d="M0 134 L140 58 M350 134 L210 58" fill="none" stroke="#e0e6ec" stroke-width="1"/>
    </svg>
  </section>

  <!-- envelope: front -->
  <section class="piece envelope envelope-front">
    <svg class="swoosh" viewBox="0 0 350 134" preserveAspectRatio="none" aria-hidden="true">
      <defs>
        <linearGradient id="gEnv" x1="0" y1="0" x2="1" y2="1">
          <stop offset="0" stop-color="#7cc6f2"/><stop offset="1" stop-color="#1f5fc4"/>
        </linearGradient>
      </defs>
      <path d="M270 134 C310 125 340 100 350 60 L350 134 Z" fill="url(#gEnv)"/>
      <path d="M250 134 C300 126 338 96 350 70" fill="none" stroke="#2f8fe0" stroke-width="1.5"/>
    </svg>
    <div class="brand"><span class="dot"></span>Silver Heron Guidance Studio</div>
    <p class="small">4810 North Calloway Avenue, Suite C 240<br>Missoula, Montana 59417</p>
  </section>

</body>
</html>
```